AVOID HOT “HARISSA” SAUCE. IN CAN

Brand Overview: Create a dynamic and eye-catching label for our new hot sauce IN CAN, “DUMEL.” Our brand is all about delivering a fiery flavor experience that combines the intensity of various peppers with unique, bold ingredients. The hot sauce targets spice enthusiasts who crave both heat and distinctive taste profiles.

Key Messages: Intensity: Emphasize the extreme heat level of the hot sauce to appeal to spice lovers.
Traditional: The taste is traditional
Flavor Fusion: Highlight the unique blend of peppers and special ingredients that sets DUMEL

Quality Ingredients: Convey the use of premium, natural ingredients to reinforce the high-quality aspect of our product.

Versatility: Communicate the sauce's versatility – perfect for various cuisines and dishes. Design Elements:

Color Palette: Use fiery reds, oranges, and yellows to convey the heat, with accents of dark and smoky tones to suggest depth of flavor.

Typography: Choose bold and legible fonts for the product name, ensuring it is easily readable from a distance.
Imagery: Incorporate visuals of flaming peppers or a stylized fire to reinforce the spicy nature of the hot sauce.
Consider using images of the key ingredients to showcase the fusion of flavors.

Texture/Background: Add a textured or gradient background to enhance visual interest and give a sense of depth.

Label Information: Product Name Hot Sauce "HARISSA" Heat Level

Indicator: Use a visual scale or iconography to indicate the spiciness level.

Ingredients: Highlight key ingredients and emphasize their quality, peppers, water, salt
SIZE: L: 12cm H: 5.5cm

Net Weight: 140g

Regulatory Information: Ensure compliance with all relevant food labeling regulations, including ingredients list, nutritional information, and contact details.

Competitor Analysis: Examine other hot sauce labels in the market to identify design trends and differentiators.
Inspiration: Consider drawing inspiration from elements like flames, peppers, or global spice motifs to create a visually striking and memorable label. Mood/Emotion: The label should evoke excitement, daring, and a sense of adventure – capturing the thrill of experiencing the intense flavor of HARISSA DUMEL Hot Sauce.

Target Audience: Spice enthusiasts, foodies, and individuals seeking a unique and bold addition to their culinary experiences.

Delivery Format: The label design should be suitable for various packaging sizes, ensuring scalability without sacrificing visual impact. Remember to balance the vibrant and intense visuals with clarity and readability and send the FONT at the moment of the delivery.
Updates

Need extra days to review

Target Market(s)

European

Font styles to use
Decorative

Colors
FFF300
FFF600
FEFA6F
FFFEC7
FFFEE8
FFC000
F8CF3A
FAE287
FDF2CF
FEFAEE
EE7325
F08F49
F5BC92
FAE3D3
FDF4ED
EB3D1F
EC4F4E
F09395
F8D3D4
FCEDEE

Requirements
Must have
• LOGO, BARCODE, Nutritional facts, INGREDIENTS

```html
<!DOCTYPE html>
<html lang="en">
<head>
<meta charset="utf-8">
<title>DUMEL Harissa Hot Sauce – Can Label</title>
<link rel="stylesheet" href="https://fonts.googleapis.com/css2?family=Bebas+Neue&family=Oswald:wght@500;600&family=Roboto+Condensed:wght@400;700&display=swap">
<style>
  :root {
    --bg: #ff9e63;
    --cream: #fdfbcf;
    --cream-edge: #eeecba;
    --orange-deep: #cf5a1c;
    --orange-mid: #e3763a;
    --orange-light: #e99058;
    --navy: #2a2f73;
    --white: #ffffff;
    --title-shadow: #9c3616;
    --ink: #1a1a1a;
    --hot-red: #e53a2f;
    --heat-1: #c8484e;
    --heat-2: #d62f47;
    --heat-3: #d8375a;
    --heat-4: #2f8a3c;
    --heat-5: #2d7f34;
    --heat-6: #1f7a36;
  }
  * { box-sizing: border-box; margin: 0; padding: 0; }
  html, body { width: 1200px; height: 1200px; overflow: hidden; }
  body { background: var(--bg); position: relative; font-family: "Roboto Condensed", sans-serif; }

  .label {
    position: absolute; left: 40px; top: 270px; width: 1120px; height: 660px;
    background: var(--cream); box-shadow: 0 18px 40px rgba(120, 50, 10, 0.25);
    overflow: hidden;
  }
  .side-panel { position: absolute; top: 0; height: 100%; background: linear-gradient(90deg, var(--cream-edge), var(--cream)); }
  .side-panel--left { left: 0; width: 300px; }

  .front-panel {
    position: absolute; left: 300px; top: 0; width: 500px; height: 100%;
    background: linear-gradient(90deg, var(--orange-light) 0%, var(--orange-mid) 30%, var(--orange-deep) 60%, var(--orange-mid) 100%);
    text-align: center;
  }
  .brand {
    position: absolute; left: 50%; top: 34px; transform: translateX(-50%);
    display: flex; align-items: center; gap: 10px;
    font-family: "Bebas Neue", sans-serif; font-size: 64px; line-height: 1; color: var(--navy);
    letter-spacing: 2px;
  }
  .brand-mark { width: 18px; height: 18px; background: var(--navy); border-radius: 50%; }
  .product-name {
    position: absolute; left: 0; right: 0; top: 112px;
    font-family: "Bebas Neue", sans-serif; font-weight: 400; color: var(--white); line-height: 0.9;
    text-shadow: 4px 4px 0 var(--title-shadow);
  }
  .product-name__main { display: block; font-size: 128px; letter-spacing: 1px; }
  .product-name__sub { display: block; font-size: 92px; letter-spacing: 1px; margin-top: 8px; }
  .artwork {
    position: absolute; left: 120px; top: 335px; width: 260px; height: 230px;
    border-radius: 45%;
    background: radial-gradient(ellipse at 50% 55%, #e22a22 0%, #d8321e 40%, #f08a2a 68%, rgba(47, 107, 45, 0.85) 100%);
  }
  .net-weight {
    position: absolute; left: 0; right: 0; bottom: 26px;
    font-family: "Oswald", sans-serif; font-weight: 500; font-size: 30px; color: var(--white);
  }

  .info-panel { position: absolute; left: 820px; top: 0; width: 300px; height: 100%; padding: 20px 20px 20px 0; }
  .nutrition {
    border: 2px solid var(--ink); background: var(--white); padding: 8px 10px;
    color: var(--ink); font-size: 10px; line-height: 1.3; height: 300px; overflow: hidden;
  }
  .nutrition__title { font-weight: 700; font-size: 15px; line-height: 1.1; }
  .nutrition__serving { border-bottom: 5px solid var(--ink); padding-bottom: 4px; margin-bottom: 4px; }
  .nutrition__row { display: flex; justify-content: space-between; border-bottom: 1px solid #999; }
  .nutrition__row--bold { font-weight: 700; }
  .nutrition__row--indent { padding-left: 10px; }
  .nutrition__note { margin-top: 5px; font-size: 9px; }

  .heat-scale { display: flex; flex-direction: column; gap: 4px; margin-top: 14px; height: 306px; }
  .heat-level { flex: 1; display: flex; gap: 12px; min-height: 0; }
  .heat-level__seg { width: 26px; flex: none; border-radius: 4px; }
  .heat-level:nth-child(1) .heat-level__seg { background: linear-gradient(var(--heat-1), var(--hot-red)); border-radius: 13px 13px 4px 4px; }
  .heat-level:nth-child(2) .heat-level__seg { background: var(--heat-2); }
  .heat-level:nth-child(3) .heat-level__seg { background: linear-gradient(var(--heat-3), #e2494a); }
  .heat-level:nth-child(4) .heat-level__seg { background: var(--heat-4); }
  .heat-level:nth-child(5) .heat-level__seg { background: var(--heat-5); }
  .heat-level:nth-child(6) .heat-level__seg { background: var(--heat-6); border-radius: 4px 4px 13px 13px; }
  .heat-level__list {
    list-style: none; display: flex; flex-direction: column; justify-content: center; gap: 3px;
    font-family: "Oswald", sans-serif; font-weight: 600; font-size: 11px; line-height: 1.15;
    color: var(--ink); text-transform: uppercase; white-space: nowrap;
  }
  .heat-level__list span { color: var(--hot-red); }
</style>
</head>
<body>
  <main class="label">
    <div class="side-panel side-panel--left"></div>

    <section class="front-panel">
      <div class="brand"><span class="brand-mark"></span>DUMEL</div>
      <h1 class="product-name">
        <span class="product-name__main">HARISSA</span>
        <span class="product-name__sub">HOT SAUCE</span>
      </h1>
      <div class="artwork" role="img" aria-label="Illustration of two red chili peppers on green leaves in front of flames"></div>
      <p class="net-weight">Net Weight: 140g</p>
    </section>

    <aside class="info-panel">
      <div class="nutrition">
        <p class="nutrition__title">Nutritional Facts<br>Valeur nutritive</p>
        <p class="nutrition__serving">Per 1 tbsp (15 ml) / Portion 15 ml<br>Servings per container: 9</p>
        <div class="nutrition__row nutrition__row--bold"><span>Calories / Calories</span><span>12</span></div>
        <div class="nutrition__row nutrition__row--bold"><span>Fat / Lipides</span><span>0.4 g</span></div>
        <div class="nutrition__row nutrition__row--indent"><span>Saturated / saturés</span><span>0 g</span></div>
        <div class="nutrition__row nutrition__row--indent"><span>Trans / trans</span><span>0 g</span></div>
        <div class="nutrition__row nutrition__row--bold"><span>Protein / Protéines</span><span>0.5 g</span></div>
        <div class="nutrition__row nutrition__row--bold"><span>Sodium / Sodium</span><span>180 mg</span></div>
        <div class="nutrition__row nutrition__row--bold"><span>Carbohydrate / Glucides</span><span>1.8 g</span></div>
        <div class="nutrition__row nutrition__row--indent"><span>Fibre / Fibres</span><span>0.6 g</span></div>
        <div class="nutrition__row nutrition__row--indent"><span>Sugar / Sucres</span><span>0.9 g</span></div>
        <p class="nutrition__note">Not a significant source of other nutrients.<br>Ingredients: red peppers, water, salt, garlic, caraway, coriander.<br>Ingrédients : piments rouges, eau, sel, ail, carvi, coriandre.</p>
      </div>

      <div class="heat-scale" role="group" aria-label="Heat level scale in Scoville units">
        <div class="heat-level">
          <div class="heat-level__seg"></div>
          <ul class="heat-level__list">
            <li>Pure capsaicin / <span>16,000,000</span></li>
            <li>Carolina reaper / <span>2,200,000</span></li>
          </ul>
        </div>
        <div class="heat-level">
          <div class="heat-level__seg"></div>
          <ul class="heat-level__list">
            <li>Naga viper / <span>1,382,118</span></li>
            <li>Bhut jolokia / <span>855,000–1,041,427</span></li>
          </ul>
        </div>
        <div class="heat-level">
          <div class="heat-level__seg"></div>
          <ul class="heat-level__list">
            <li>Red savina habanero / <span>350,000–580,000</span></li>
          </ul>
        </div>
        <div class="heat-level">
          <div class="heat-level__seg"></div>
          <ul class="heat-level__list">
            <li>Bird's eye / <span>100,000–300,000</span></li>
            <li>Thai / <span>50,000–100,000</span></li>
          </ul>
        </div>
        <div class="heat-level">
          <div class="heat-level__seg"></div>
          <ul class="heat-level__list">
            <li>Cayenne / <span>30,000–50,000</span></li>
            <li>Serrano / <span>10,000–23,000</span></li>
          </ul>
        </div>
        <div class="heat-level">
          <div class="heat-level__seg"></div>
          <ul class="heat-level__list">
            <li>Poblano / <span>1,000–2,000</span></li>
            <li>Pepperoncini / <span>100–500</span></li>
          </ul>
        </div>
      </div>
    </aside>
  </main>
</body>
</html>
```